Cash Balance Retirement Plan Services Page

We are looking to have a services/landing page created for one of our offerings. The goal of the page is to explain a relatively complex service (advanced retirement plan) by highlighting the benefits and uses for the plan such that it tells a story that encourages individuals and businesses that would benefit from the plans to reach out.

The page will be used both as a landing page (though secondarily) and as a page that many of our partners will show to their clients in order to generate interest. We help other people closes these deals so we want it to handle both.

Overall, we would want the page to incorporate the following sections/areas.
1. Headline and a place for a video at the top
2. Explanation of what a cash balance plan is (a paragraph or two)
3. These five benefits: These are the 7 we usually use, but only include five at a time so only need room for five.
a. Highest Tax Deductible Contributions Allowed
b. Significantly reduce your taxes
c. Potential Negative “Net Cost”
d. Owner & Executive Weighted Benefits
e. Retain and Attract Top Talen
f. Catch Up On decades of low retirement savings in a matter of years
g. Potential for life time income
4. A section comparing the contribution limits allowed for each plan type (Please see attached image as an example).
5. A place for a table of contribution amounts (This will just be an image. Also, attached).
6. A place for a compare table
6. Who should consider such a plan
7. Occasional banners for call to actions
8. FAQ

Our primary audience for this project are successful small business owners with a particular focus on medical professionals (doctors, chiropractors, dentists, plastic surgeons, etc.). In generally, they will be between 45 and 65 years old and earn $150k or more.

Because we work a lot with financial, business strategy, and insurance based products that require a significant investment by the client trust, professionalism, and sophistication are important attributes we wish to portray in the design of the page. Our preferred colors are blue or green. Though we are still working on figuring out the color scheme so your input as a designer is welcomed as your creativity can help us communicate the attributes we seek to embody for our clients.

In the attached document, I have included some additional information about the service itself if it helps to have some context, as well as a more flushed out outline of the details above.

Importantly, I am not a marketer so any creative input is always welcome if there is a best practice we are not incorporating in either our design requests or outline.

Here is the URL for our current page: https://www.brightoakpartners.com/doctorcashplan

Please don't let this page be your muse. We're trying to get away from it for a reason :) But it still will hopefully provide some helpful information, copy examples, and context.

Additionally, please don't feel like you need to read the full cash balance explanation. That's only if context will be helpful.

We are also going through a rebranding so please don't rely on the colors from the BrightOakPartners logo you may see on the website. I've attached two sample logos for the rebrand for context.

```html
<!DOCTYPE html>
<html lang="en">
<head>
<meta charset="utf-8">
<title>BrightOakPartners – Cash Balance Plan</title>
<link href="https://fonts.googleapis.com/css2?family=Open+Sans:wght@400;600;700&display=swap" rel="stylesheet">
<style>
:root{
  --blue:#1565a7;
  --blue-dark:#0f4f86;
  --navy:#1b1f8c;
  --charcoal:#47474a;
  --footer:#3d3d40;
  --gray-bg:#e8e9ec;
  --row-a:#c8d2ea;
  --row-b:#e2e7f3;
  --text:#3b3b3b;
  --white:#fff;
}
*{box-sizing:border-box;margin:0;padding:0}
html,body{width:1200px;height:4992px;overflow:hidden}
body{font-family:"Open Sans",sans-serif;color:var(--text);background:var(--white);position:relative}
.abs{position:absolute}
section,header,footer{position:absolute;left:0;width:1200px}

/* top bar + header */
.topbar{top:0;height:38px}
.topbar__band{position:absolute;right:0;top:0;width:640px;height:38px;background:var(--charcoal)}
.topbar__call{position:absolute;left:558px;top:0;width:290px;height:38px;background:var(--blue);clip-path:polygon(0 0,100% 0,94% 100%,6% 100%);display:flex;align-items:center;justify-content:center;gap:10px;color:#fff;font-size:15px}
.topbar__mail{position:absolute;left:878px;top:0;height:38px;display:flex;align-items:center;gap:12px;color:#fff;font-size:15px}
.site-header{top:0;height:115px}
.brand{position:absolute;left:110px;top:66px;display:flex;align-items:center;gap:8px;font-weight:700;font-size:19px;color:#2a2a2a;white-space:nowrap}
.brand__dot{width:18px;height:18px;border-radius:50%;background:var(--charcoal);flex:none}
.nav{position:absolute;left:370px;top:64px;display:flex;gap:30px;font-size:16px;color:#333}
.nav .active{color:var(--blue);font-weight:600;border-bottom:2px solid var(--blue)}
.btn{display:inline-flex;align-items:center;justify-content:center;background:var(--blue);color:#fff;font-weight:600;border-radius:4px;font-size:16px}
.site-header .btn{position:absolute;left:948px;top:56px;width:142px;height:42px}

/* hero */
.hero{top:115px;height:618px;overflow:hidden}
.hero__photo{position:absolute;inset:0;background:linear-gradient(100deg,#1d4f86 0%,#3f78ad 45%,#a9c3da 75%,#d9e3ec 100%)}
.hero__text{position:absolute;left:110px;top:178px;color:#fff}
.hero__text p{font-size:56px;font-weight:400;line-height:1.1}
.hero__text h1{font-size:64px;font-weight:600;line-height:1.3}
.hero__btn{position:absolute;left:110px;top:381px;width:146px;height:48px;border:2px solid #fff;border-radius:6px;color:#fff;font-size:17px;display:flex;align-items:center;justify-content:center}
.hero__arrow{position:absolute;top:290px;width:36px;height:36px;border:2px solid #fff;border-radius:50%;display:flex;align-items:center;justify-content:center}
.hero__wave{position:absolute;left:0;bottom:0;width:1200px;height:80px}

/* section titles */
.title{position:absolute;left:0;width:1200px;text-align:center;color:var(--blue);font-size:42px;font-weight:400}
.title span::before,.title span::after{content:"";display:inline-block;width:44px;height:2px;background:var(--charcoal);vertical-align:middle;margin:0 20px}

/* cash balance */
.cbp{top:733px;height:537px}
.cbp__frame{position:absolute;left:128px;top:92px;width:333px;height:371px;background:var(--charcoal)}
.cbp__photo{position:absolute;left:110px;top:75px;width:334px;height:373px;background:linear-gradient(160deg,#8da2b3,#dfe6ec 55%,#5b6f86)}
.cbp h2{position:absolute;left:514px;top:102px;font-size:44px;font-weight:400;color:var(--blue)}
.cbp h2::after{content:"";display:inline-block;width:44px;height:2px;background:var(--charcoal);vertical-align:middle;margin-left:18px}
.cbp p{position:absolute;left:516px;top:180px;width:574px;font-size:15.5px;line-height:28.5px;text-align:justify}
.cbp .btn{position:absolute;left:518px;top:380px;width:142px;height:43px}

/* benefits */
.benefits{top:1270px;height:741px;background:linear-gradient(180deg,#e4e6ea,#eef0f2 60%,#e3e5e9)}
.card{position:absolute;color:#fff;font-weight:700;font-size:16.5px;line-height:29px}
.card--blue{background:var(--blue)}
.card--dark{background:var(--charcoal)}
.card--tall{height:273px;width:306px;display:flex;flex-direction:column;align-items:center;text-align:center;padding-top:36px}
.card--tall .icon{margin-bottom:22px}
.card--wide{height:182px;display:flex;align-items:center;padding-left:52px;gap:40px}
.icon{width:116px;height:116px;border-radius:50%;background:#fff;border:8px solid #c9ccd1;display:flex;align-items:center;justify-content:center;flex:none}

/* comparison */
.compare{top:2011px;height:632px}
.compare .title{line-height:70px}
.compare p{position:absolute;left:110px;top:348px;width:394px;font-size:15.5px;line-height:28.5px;text-align:justify}
.chart__frame{position:absolute;left:539px;top:296px;width:537px;height:262px;background:var(--blue-dark)}
.chart{position:absolute;left:551px;top:285px;width:537px;height:264px;background:#fff;border:1px solid #cfd2d6;box-shadow:0 3px 12px rgba(0,0,0,.2)}

/* table */
.table-sec{top:2643px;height:591px;background:var(--gray-bg)}
.data{position:absolute;left:171px;top:172px;width:855px;border-collapse:collapse;font-size:20px;box-shadow:0 0 0 5px #fff;background:#fff}
.data th{background:var(--navy);color:#fff;text-align:left;vertical-align:top;font-weight:600;padding:8px 9px;line-height:28px;height:130px;border-right:2px solid #fff}
.data td{padding:0 9px;height:38.5px;border-right:2px solid #fff;border-top:1px solid #fff;color:#222}
.data tr:nth-child(odd) td{background:var(--row-a)}
.data tr:nth-child(even) td{background:var(--row-b)}
.data td.strong{font-weight:700}

/* who */
.who{top:3234px;height:597px}
.who ul{position:absolute;left:120px;top:172px;width:460px;list-style:none;font-size:15.5px;line-height:28px}
.who li{position:relative;padding-left:18px;margin-bottom:12px}
.who li::before{content:"";position:absolute;left:0;top:11px;width:7px;height:7px;border-radius:50%;background:var(--blue)}
.who .btn{position:absolute;left:110px;top:489px;width:142px;height:42px}
.who__outline{position:absolute;left:669px;top:174px;width:419px;height:343px;border:2px solid var(--charcoal)}
.who__photo{position:absolute;left:683px;top:188px;width:391px;height:316px;background:linear-gradient(120deg,#5a87a8,#dce4ea 50%,#6d93b4)}

/* faq */
.faq{top:3831px;height:801px;background:linear-gradient(180deg,#eeeff1,#f3f3f4)}
.faq__item{position:absolute;left:110px;width:978px;background:#fff;box-shadow:0 2px 8px rgba(0,0,0,.08)}
.faq__q{height:80px;display:flex;align-items:center;justify-content:space-between;padding:0 14px 0 32px;font-size:15.5px;color:#333}
.faq__toggle{width:68px;height:50px;background:#e9edf3;display:flex;align-items:center;justify-content:center;border:1px solid #dfe3ea}
.faq__item--open .faq__q{background:#dfe9f5}
.faq__item--open .faq__toggle{background:#fff}
.faq__a{padding:24px 32px 40px;font-size:15.5px;color:#333}

/* footer */
.site-footer{top:4632px;height:360px;background:var(--footer);color:#fff}
.footer__brand{position:absolute;left:0;width:1200px;top:66px;display:flex;justify-content:center;align-items:center;gap:12px;font-size:26px;font-weight:600}
.footer__brand .brand__dot{background:#fff;width:22px;height:22px}
.footer__nav{position:absolute;left:0;width:1200px;top:160px;display:flex;justify-content:center;gap:30px;font-size:16px}
.contact{position:absolute;top:228px;display:flex;gap:14px;font-size:16px;line-height:25px}
.contact b{font-weight:600;text-transform:uppercase}
.footer__rule{position:absolute;left:110px;top:292px;width:980px;height:1px;background:#5a5a5e}
.footer__copy{position:absolute;left:0;width:1200px;top:324px;text-align:center;font-size:14.5px}
</style>
</head>
<body>

<header class="site-header">
  <div class="topbar abs" style="left:0;width:1200px">
    <div class="topbar__band"></div>
    <div class="topbar__call">
      <svg width="18" height="18" viewBox="0 0 24 24"><path fill="#fff" d="M6.6 10.8a15.1 15.1 0 006.6 6.6l2.2-2.2c.3-.3.7-.4 1-.2 1.1.4 2.3.6 3.6.6.6 0 1 .4 1 1V20c0 .6-.4 1-1 1A17 17 0 013 4c0-.6.4-1 1-1h3.5c.6 0 1 .4 1 1 0 1.3.2 2.5.6 3.6.1.3 0 .7-.2 1z"/></svg>
      Call Us: +1 555-014-2290
    </div>
    <div class="topbar__mail">
      <svg width="22" height="16" viewBox="0 0 22 16"><rect x="1" y="1" width="20" height="14" fill="none" stroke="#fff" stroke-width="2"/><path d="M1 1l10 8 10-8" fill="none" stroke="#fff" stroke-width="2"/></svg>
      info@brightoakpartners.com
    </div>
  </div>
  <div class="brand"><span class="brand__dot"></span>BrightOakPartners</div>
  <nav class="nav">
    <span class="active">Home</span><span>Cash Balance Plan</span><span>Benefits</span><span>Compare Table</span><span>FAQs</span>
  </nav>
  <span class="btn">Get A Quote</span>
</header>

<section class="hero">
  <div class="hero__photo" role="img" aria-label="Smiling doctor in a white coat with a stethoscope in a clinic"></div>
  <div class="hero__text">
    <p>Welcome to</p>
    <h1>BrightOakPartners</h1>
  </div>
  <span class="hero__btn">Get A Quote</span>
  <span class="hero__arrow" style="left:38px"><svg width="18" height="14" viewBox="0 0 18 14"><path d="M17 7H2M7 1L1 7l6 6" fill="none" stroke="#fff" stroke-width="2"/></svg></span>
  <span class="hero__arrow" style="left:1126px"><svg width="18" height="14" viewBox="0 0 18 14"><path d="M1 7h15M11 1l6 6-6 6" fill="none" stroke="#fff" stroke-width="2"/></svg></span>
  <svg class="hero__wave" viewBox="0 0 1200 80" preserveAspectRatio="none">
    <path d="M0 80 L0 70 Q300 60 600 30 Q900 58 1200 38 L1200 80 Z" fill="#1565a7"/>
    <path d="M0 80 L0 78 Q300 70 600 42 Q900 66 1200 50 L1200 80 Z" fill="#fff"/>
  </svg>
</section>

<section class="cbp">
  <div class="cbp__frame"></div>
  <div class="cbp__photo" role="img" aria-label="Two doctors discussing a tablet in a hospital corridor"></div>
  <h2>Cash Balance Plan</h2>
  <p>Lorem ipsum dolor sit amet, consectetur adipiscing elit, sed do eiusmod tempor incididunt ut labore et dolore magna aliqua. Ut enim ad minim veniam, quis nostrud exercitation ullamco laboris nisi ut aliquip ex ea commodo consequat. Duis aute irure dolor in reprehenderit in voluptate velit esse cillum dolore eu fugiat nulla pariatur. Excepteur sint occaecat cupidatat non proident, sunt in culpa qui officia deserunt mollit anim id est laborum.</p>
  <span class="btn">Learn More</span>
</section>

<section class="benefits">
  <h2 class="title" style="top:68px"><span>Our Benefits</span></h2>
  <div class="card card--blue card--tall" style="left:124px;top:171px">
    <span class="icon"><svg width="60" height="60" viewBox="0 0 60 60" fill="none" stroke="#1565a7" stroke-width="2.5"><circle cx="36" cy="20" r="14"/><path d="M30 27l12-14"/><circle cx="31" cy="15" r="2"/><circle cx="41" cy="25" r="2"/><ellipse cx="18" cy="40" rx="10" ry="3"/><path d="M8 40v12c0 2 20 2 20 0V40M8 46c0 2 20 2 20 0"/></svg></span>
    Highest Tax Deductible<br>Contributions Allowed
  </div>
  <div class="card card--dark card--tall" style="left:446px;top:171px">
    <span class="icon"><svg width="60" height="60" viewBox="0 0 60 60" fill="none" stroke="#47474a" stroke-width="2.5"><rect x="8" y="10" width="44" height="30"/><path d="M16 20h8M30 20h14M16 30h28"/><circle cx="20" cy="50" r="4"/><circle cx="38" cy="50" r="4"/><path d="M23 47l12-14M35 47L23 33"/></svg></span>
    Significantly reduce your<br>taxes
  </div>
  <div class="card card--blue card--tall" style="left:768px;top:171px">
    <span class="icon"><svg width="60" height="60" viewBox="0 0 60 60" fill="none" stroke="#1565a7" stroke-width="2.5"><rect x="8" y="24" width="7" height="26"/><rect x="20" y="30" width="7" height="20"/><rect x="32" y="36" width="7" height="14"/><rect x="44" y="42" width="7" height="8"/><path d="M8 12l20 10 18 8M46 24l2 7-7 1"/></svg></span>
    Potential Negative “Net<br>Cost”
  </div>
  <div class="card card--blue card--wide" style="left:124px;top:460px;width:465px">
    <span class="icon"><svg width="60" height="60" viewBox="0 0 60 60" fill="none" stroke="#1565a7" stroke-width="2.5"><path d="M22 12v12M16 18h12M38 8v10M33 13h10M30 26v10M25 31h10"/><path d="M6 40h10l10 4h12c3 0 3 4 0 4H26M16 52l20 2 18-10c2-2 0-5-3-4l-13 6"/></svg></span>
    <span>Owner &amp; Executive<br>Weighted Benefits</span>
  </div>
  <div class="card card--dark card--wide" style="left:611px;top:460px;width:463px">
    <span class="icon"><svg width="60" height="60" viewBox="0 0 60 60" fill="none" stroke="#47474a" stroke-width="2.5"><path d="M46 22a18 18 0 10-2 20"/><path d="M42 14l4 8-9 1"/><path d="M14 30a16 16 0 0030 8" stroke-dasharray="2 5"/></svg></span>
    <span>Retain and Attract Top<br>Talen</span>
  </div>
</section>

<section class="compare">
  <h2 class="title" style="top:77px">Comparing The Contribution Limits<br><span>Allowed For Each Plan Type</span></h2>
  <p>Lorem ipsum dolor sit amet, consectetur adipiscing elit, sed do eiusmod tempor incididunt ut labore et dolore magna aliqua. Ut enim ad minim veniam, quis nostrud exercitation ullamco laboris nisi ut aliquip ex ea commodo consequat.</p>
  <div class="chart__frame"></div>
  <svg class="chart" viewBox="0 0 537 264" font-family="Arial, sans-serif" font-weight="700" font-size="8.5" fill="#222">
    <text x="68" y="152" text-anchor="middle">Annual</text>
    <text x="68" y="162" text-anchor="middle">Contributio</text>
    <text x="68" y="172" text-anchor="middle">ns</text>
    <text x="68" y="182" text-anchor="middle">Limits</text>
    <text x="133" y="157" text-anchor="middle">$6,000</text>
    <text x="133" y="166" text-anchor="middle">($7000)</text>
    <rect x="113" y="172" width="40" height="10" fill="#7bc86c"/>
    <text x="133" y="196" text-anchor="middle">IRA</text>
    <text x="225" y="145" text-anchor="middle">$20,500</text>
    <text x="225" y="154" text-anchor="middle">($27,000)</text>
    <rect x="205" y="160" width="40" height="22" fill="#22a83a"/>
    <text x="225" y="196" text-anchor="middle">401(k)</text>
    <text x="314" y="126" text-anchor="middle">$61,000</text>
    <rect x="294" y="134" width="40" height="48" fill="#8ab9ee"/>
    <text x="314" y="196" text-anchor="middle">Profit</text>
    <text x="314" y="205" text-anchor="middle">Sharin</text>
    <text x="314" y="214" text-anchor="middle">g</text>
    <text x="406" y="34" text-anchor="middle">$416,000</text>
    <rect x="386" y="42" width="40" height="140" fill="#1f63d0"/>
    <text x="406" y="196" text-anchor="middle">Cash</text>
    <text x="406" y="205" text-anchor="middle">Balance</text>
    <text x="406" y="214" text-anchor="middle">Plan</text>
    <g font-weight="400" font-size="7.5" text-anchor="middle">
      <text x="479" y="66">*Your</text><text x="479" y="75">contribution</text><text x="479" y="84">limits will be</text><text x="479" y="93">based on age</text><text x="479" y="102">and salary</text><text x="479" y="111">and may not</text><text x="479" y="120">reach the max</text><text x="479" y="129">contribution</text><text x="479" y="138">amount.</text>
    </g>
  </svg>
</section>

<section class="table-sec">
  <h2 class="title" style="top:66px"><span>Table Of Contribution Amounts</span></h2>
  <table class="data">
    <thead><tr>
      <th style="width:141px">Starting Plan at Age:</th>
      <th style="width:141px">Max Monthly Retirement Benefit:</th>
      <th style="width:140px">Lump Sum at Retirement:</th>
      <th style="width:155px">Illustrative Contribution Limits:</th>
      <th style="width:125px">Estimated Tax Savings:</th>
      <th>“Net Cost” after Tax Savings:</th>
    </tr></thead>
    <tbody>
      <tr><td>40</td><td>$20,417</td><td>$2,959,124</td><td class="strong">$141,358</td><td>$56,543</td><td>$84,814</td></tr>
      <tr><td>45</td><td>$20,417</td><td>$2,959,124</td><td class="strong">$178,753</td><td>$71,501</td><td>$107,252</td></tr>
      <tr><td>50</td><td>$20,417</td><td>$2,959,124</td><td class="strong">$246,962</td><td>$98,784</td><td>$148,177</td></tr>
      <tr><td>55</td><td>$20,417</td><td>$2,959,124</td><td class="strong">$382,181</td><td>$152,872</td><td>$229,308</td></tr>
      <tr><td>60</td><td>$10,208</td><td>$1,479,561</td><td class="strong">$400,418</td><td>$160,192</td><td>$240,225</td></tr>
    </tbody>
  </table>
</section>

<section class="who">
  <h2 class="title" style="top:60px"><span>Who should consider such a plan</span></h2>
  <ul>
    <li>Lorem ipsum dolor sit amet, consectetur adipiscing elit, sed do eiusmod tempor incididunt</li>
    <li>Lorem ipsum dolor sit amet, consectetur adipiscing elit</li>
    <li>Lorem ipsum dolor sit amet, consectetur adipiscing elit, sed do eiusmod tempor incididunt</li>
    <li>Lorem ipsum dolor sit amet, consectetur adipiscing elit</li>
    <li>Lorem ipsum dolor sit amet, consectetur adipiscing elit, sed do eiusmod tempor incididunt</li>
  </ul>
  <span class="btn">Get Started</span>
  <div class="who__outline"></div>
  <div class="who__photo" role="img" aria-label="Senior doctor standing in front of his medical team"></div>
</section>

<section class="faq">
  <h2 class="title" style="top:68px"><span>FAQs</span></h2>
  <div class="faq__item" style="top:167px">
    <div class="faq__q">What is your company slogan or mission statement?<span class="faq__toggle"><svg width="20" height="20"><path d="M10 2v16M2 10h16" stroke="#333" stroke-width="2"/></svg></span></div>
  </div>
  <div class="faq__item faq__item--open" style="top:264px">
    <div class="faq__q">How would you describe your business in one sentence? What is the basic function of your product/service?<span class="faq__toggle"><svg width="20" height="20"><path d="M2 10h16" stroke="#333" stroke-width="2"/></svg></span></div>
    <div class="faq__a">We operate in specialized retirement services and insurance products designed for small and medium size businesses.</div>
  </div>
  <div class="faq__item" style="top:446px">
    <div class="faq__q">What is your goal with this content?<span class="faq__toggle"><svg width="20" height="20"><path d="M10 2v16M2 10h16" stroke="#333" stroke-width="2"/></svg></span></div>
  </div>
  <div class="faq__item" style="top:543px">
    <div class="faq__q">What are the unique selling points of your company?<span class="faq__toggle"><svg width="20" height="20"><path d="M10 2v16M2 10h16" stroke="#333" stroke-width="2"/></svg></span></div>
  </div>
  <div class="faq__item" style="top:640px">
    <div class="faq__q">Is there a specific tone of voice you want?<span class="faq__toggle"><svg width="20" height="20"><path d="M10 2v16M2 10h16" stroke="#333" stroke-width="2"/></svg></span></div>
  </div>
</section>

<footer class="site-footer">
  <div class="footer__brand"><span class="brand__dot"></span>BrightOakPartners</div>
  <nav class="footer__nav"><span>Home</span><span>Cash Balance Plan</span><span>Benefits</span><span>Compare Table</span><span>FAQs</span></nav>
  <div class="contact" style="left:188px">
    <svg width="18" height="24" viewBox="0 0 18 24"><path d="M9 1a8 8 0 00-8 8c0 6 8 14 8 14s8-8 8-14a8 8 0 00-8-8z" fill="none" stroke="#fff" stroke-width="1.8"/><circle cx="9" cy="9" r="3" fill="none" stroke="#fff" stroke-width="1.8"/></svg>
    <div><b>Address</b><br>BrightOakPartners, address here</div>
  </div>
  <div class="contact" style="left:530px">
    <svg width="22" height="18" viewBox="0 0 22 18"><rect x="1" y="1" width="20" height="16" fill="none" stroke="#fff" stroke-width="1.8"/><path d="M1 1l10 8 10-8" fill="none" stroke="#fff" stroke-width="1.8"/></svg>
    <div><b>Email</b><br>info@brightoakpartners.com</div>
  </div>
  <div class="contact" style="left:852px">
    <svg width="20" height="20" viewBox="0 0 24 24"><path fill="none" stroke="#fff" stroke-width="1.8" d="M6.6 10.8a15.1 15.1 0 006.6 6.6l2.2-2.2c.3-.3.7-.4 1-.2 1.1.4 2.3.6 3.6.6.6 0 1 .4 1 1V20c0 .6-.4 1-1 1A17 17 0 013 4c0-.6.4-1 1-1h3.5c.6 0 1 .4 1 1 0 1.3.2 2.5.6 3.6.1.3 0 .7-.2 1z"/></svg>
    <div><b>Phone</b><br>+1 555-014-2290</div>
  </div>
  <div class="footer__rule"></div>
  <div class="footer__copy">2022 BrightOakPartners. All Rights Reserved.</div>
</footer>

</body>
</html>
```